Dynamic and Revolutionary Training Company Requires Stationery Design Project

We are a training company who deliver training both online and face to face.

We train in:
~ Industry Training: Earth Moving Machinery, Cranes, Work at Heights, Confined Spaces, Elevating Work Platforms, Forklift etc.
~ Food Hygiene / Safety
~ Responsible Service of Alcohol / Gambling

Our company is interested in sourcing stationery designs for:

* Pens
These will be used in classroom training courses but also given away in advertising 'packs'

* Presentation folders
These can be either bi or tri fold cardboard folders. Promotional materials / leaflets will be placed inside these folders and given away in advertising 'packs'

* Letterhead
We need to update our old / outdated letterhead

* Exercise Book Covers
These exercise books will be used by students in our face to face training courses.

* With Compliments Slip
In 100+ envelopes we send each day we currently add a business card. We are now going to add a with with compliments slip with an offer / promotion instead.

* Pull Up Banner
Front of stall display at expos / trade shows.

* Flyers
We would like a template design for a DL sized flyer. We offer training in over 30 courses, so if we had a standard template that could be adapted to each training course we would achieve consistency in advertising.
Flyers would need the same / similar front (with space for a picture) and course information could be placed on the back.

Because of our extensive (and ever expanding) scope of training, certain products (folders, exercise books) will allow us to list some / all our training courses.
Other advertising mediums will obviously only allow us to display our logo and slogan (pens etc).

Please find attached our company logo.
Company slogan -
Updates

Good Morning All,

I apologise for this glaring oversight.

I unfortunately failed to mention that our primary 'business colour' (obviously outside the logo) is blue. 

Traditionally, the blue I refer to is a lightish blue as can be seen on our website banner: www.quorvelskills.edu.au 
We are however moving into a new premises which has navy blue carpet, so we would like to move more towards a navy blue.

We would also like to adjust several sliders, significantly more towards:
* elegant
* personable

And somewhat more towards:
* colourful

Sorry for any inconvenience designers :(

Regards,
Tam

Closing day tomorrow.

Only received designs from 2 designers thus far.

Last chance today to submit designs.............................

Target Market(s)

Employed / unemployed persons looking to upskill, companies / organisations looking for a quality training provider.

Industry/Entity Type

Advertising

Requirements
Must have
• More than happy to be guided by designer.

I would like to see the letterhead also involve a footer - of some sort.

Logo colours are original since company inception so must remain.

Slogan - we do have one, however our advertising has never had it as a major focus.
Nice to have
• Most written correspondence we send via email (statements of attainment, invoices etc) has a Quorvel Training watermark across it.
If possible and it looks appropriate in your opinion, the larger advertising (folders, exercise books) could MAYBE have that as well.

```html
<!DOCTYPE html>
<html lang="en">
<head>
<meta charset="utf-8">
<title>Quorvel Training Stationery</title>
<link href="https://fonts.googleapis.com/css2?family=Open+Sans:wght@400;600;700&display=swap" rel="stylesheet">
<style>
  :root {
    --olive: #a9a23a;
    --navy: #0b2a6e;
    --ink: #1e1e1e;
    --paper: #ffffff;
    --backdrop: #d9d9d9;
    --label: #ffffff;
  }
  * { margin: 0; padding: 0; box-sizing: border-box; }
  html, body { width: 1200px; height: 1039px; overflow: hidden; }
  body {
    position: relative;
    background: var(--backdrop);
    font-family: "Open Sans", Arial, sans-serif;
    color: var(--ink);
  }
  .item-label {
    position: absolute;
    color: var(--label);
    font: 700 18px "Open Sans", Arial, sans-serif;
    text-shadow: 0 1px 3px rgba(0,0,0,.45);
  }
  .sheet {
    position: absolute;
    background: var(--paper);
    box-shadow: 0 6px 14px rgba(0,0,0,.3);
    overflow: hidden;
  }
  .letterhead { left: 43px; top: 63px; width: 643px; height: 908px; }
  .slip { left: 450px; top: 258px; width: 700px; height: 311px; }

  .brand { display: flex; align-items: center; gap: 10px; position: absolute; }
  .brand-square { width: 22px; height: 22px; background: var(--olive); }
  .brand-name { font-weight: 700; color: var(--olive); letter-spacing: .5px; white-space: nowrap; }
  .letterhead .brand { left: 41px; top: 104px; }
  .letterhead .brand-name { font-size: 24px; }
  .slip .brand { left: 30px; top: 40px; }
  .slip .brand .brand-square { width: 16px; height: 16px; }
  .slip .brand-name { font-size: 17px; }

  .contact { position: absolute; left: 451px; top: 36px; font-size: 10px; line-height: 14px; }
  .contact li { list-style: none; display: flex; align-items: center; gap: 6px; }
  .contact .icon { width: 9px; height: 9px; fill: var(--olive); }
  .address { margin-top: 7px; }
  .business-ids { margin-top: 6px; }

  .slip-address { position: absolute; left: 30px; top: 95px; font-size: 10px; line-height: 13px; }
  .slip-title { position: absolute; right: 31px; top: 28px; font-size: 17px; }

  .footer-band { position: absolute; left: 0; right: 0; bottom: 0; background: var(--navy); }
  .footer-rule { position: absolute; left: 0; right: 0; height: 6px; background: var(--olive); }
  .letterhead .footer-band { height: 60px; }
  .letterhead .footer-rule { bottom: 70px; }
  .slip .footer-band { height: 44px; }
  .slip .footer-rule { bottom: 52px; }

  .pen-print {
    position: absolute; left: 760px; top: 870px; width: 380px; height: 56px;
    background: var(--paper); border-radius: 28px;
    box-shadow: 0 4px 10px rgba(0,0,0,.3);
    display: flex; align-items: center; justify-content: center; gap: 10px;
  }
  .pen-print .brand-square { width: 16px; height: 16px; }
  .pen-print .brand-name { font-size: 20px; }
</style>
</head>
<body>
  <span class="item-label" style="left:43px;top:30px;">Letterhead</span>
  <span class="item-label" style="left:906px;top:212px;">With Compliments Slip</span>
  <span class="item-label" style="left:744px;top:845px;">Pen</span>

  <section class="sheet letterhead">
    <div class="brand">
      <span class="brand-square"></span>
      <span class="brand-name">QUORVEL TRAINING</span>
    </div>
    <ul class="contact">
      <li><svg class="icon" viewBox="0 0 10 10"><path d="M1 3c0-2 8-2 8 0v1H7V3H3v1H1zM2 5h6l1 4H1z"/></svg>(07) 5550 1112</li>
      <li><svg class="icon" viewBox="0 0 10 10"><path d="M3 0h4v3H3zM1 3h8v5H7v2H3V8H1z"/></svg>(07) 5550 8809</li>
      <li><svg class="icon" viewBox="0 0 10 10"><circle cx="5" cy="5" r="4.5"/></svg>support@quorvelskills.edu.au</li>
      <li><svg class="icon" viewBox="0 0 10 10"><circle cx="5" cy="5" r="4.5"/></svg>www.quorvelskills.edu.au</li>
      <li class="address">14 Harlow Street, Eastbrook</li>
      <li>PO Box 3150 Eastbrook South</li>
      <li class="business-ids">ABN: 12 345 678 901 - RTO: 40217</li>
    </ul>
    <div class="footer-rule"></div>
    <div class="footer-band"></div>
  </section>

  <section class="sheet slip">
    <div class="brand">
      <span class="brand-square"></span>
      <span class="brand-name">QUORVEL TRAINING</span>
    </div>
    <p class="slip-address">14 Harlow Street, Eastbrook<br>PO Box 3150 Eastbrook South</p>
    <p class="slip-title">With Compliments</p>
    <div class="footer-rule"></div>
    <div class="footer-band"></div>
  </section>

  <div class="pen-print">
    <span class="brand-square"></span>
    <span class="brand-name">QUORVEL TRAINING</span>
  </div>
</body>
</html>
```